Coralbend Pastoral Traders Business Cards

We require business cards revamped with our logo. A few details we would like to use.

1. Round Edges
2. Our logo over the top of a wagyu cattle background photo on one side of the card

Other side of the card has the below details.

1. Person Name (First & Last)
2. Job Position
3. Mobile Number
4. Email Address
5. Website Address

Simple & Neat.

Target Market(s)

Sales

Industry/Entity Type

Agriculture

Contact Information for Business Card

CORALBEND PASTORAL TRADERS

Colors

Designer to choose colors to be used in the design.

Requirements
Must have
• Company Logo

```html
<!DOCTYPE html>
<html lang="en">
<head>
<meta charset="utf-8">
<title>Coralbend Pastoral Traders – Business Cards</title>
<link rel="stylesheet" href="https://fonts.googleapis.com/css2?family=Cinzel:wght@600&family=Montserrat:wght@400;500&display=swap">
<style>
  :root {
    --backdrop: #d6d7da;
    --card: #ffffff;
    --maroon: #6b1428;
    --maroon-edge: #5a0f1f;
    --ink: #2b2b2b;
    --blush: #ecdede;
  }
  * { box-sizing: border-box; margin: 0; padding: 0; }
  html, body {
    width: 1200px; height: 939px; overflow: hidden;
    background: radial-gradient(circle at 50% 45%, #e4e5e7, var(--backdrop));
  }
  .card {
    position: absolute;
    width: 560px; height: 320px;
    background: var(--card);
    border-radius: 30px;
    border-bottom: 3px solid var(--maroon-edge);
    box-shadow: 0 14px 30px rgba(0,0,0,0.18);
    overflow: hidden;
  }
  .card--front { left: 110px; top: 110px; }
  .card--back  { left: 530px; top: 500px; }

  .brand {
    display: flex; align-items: center; gap: 10px;
    font-family: "Cinzel", serif; font-weight: 600;
    color: var(--maroon); letter-spacing: 0.04em; line-height: 1.1;
  }
  .brand__dot {
    width: 16px; height: 16px; border-radius: 50%;
    background: var(--maroon); flex: none;
  }
  .card--front .brand {
    position: absolute; left: 0; right: 0; top: 50%;
    transform: translateY(-50%); justify-content: center; font-size: 26px;
  }
  .card--back .brand {
    position: absolute; left: 36px; top: 150px; font-size: 15px; width: 220px;
  }
  .card--back .brand__dot { width: 12px; height: 12px; }

  .herd-backdrop {
    position: absolute; left: 150px; top: 150px;
    width: 220px; height: 170px;
    background: radial-gradient(ellipse at 45% 55%, var(--blush), rgba(236,222,222,0) 72%);
  }

  .person { position: absolute; left: 290px; top: 52px; }
  .person__name {
    font-family: "Cinzel", serif; font-weight: 600;
    font-size: 21px; color: var(--maroon); letter-spacing: 0.03em;
  }
  .person__role {
    font-family: "Montserrat", sans-serif; font-size: 12px;
    color: var(--ink); margin-top: 2px; padding-left: 12px;
  }

  .contacts {
    position: absolute; left: 318px; top: 190px; list-style: none;
    font-family: "Montserrat", sans-serif; font-size: 11.5px; color: var(--ink);
  }
  .contacts li { display: flex; align-items: center; gap: 8px; margin-bottom: 9px; }
  .contacts svg { width: 12px; height: 12px; fill: var(--maroon); flex: none; }
  .contacts .phone { letter-spacing: 0.18em; }
</style>
</head>
<body>

<section class="card card--front" aria-label="Card front">
  <div class="brand"><span class="brand__dot"></span>Coralbend Pastoral Traders</div>
</section>

<section class="card card--back" aria-label="Card back">
  <div class="herd-backdrop" role="img" aria-label="Faint silhouette of a standing cattle beast on a grassy rise"></div>

  <div class="brand"><span class="brand__dot"></span>Coralbend Pastoral Traders</div>

  <div class="person">
    <p class="person__name">Callum Whitford</p>
    <p class="person__role">Director</p>
  </div>

  <ul class="contacts">
    <li>
      <svg viewBox="0 0 24 24" aria-hidden="true"><path d="M6.6 10.8a15.1 15.1 0 0 0 6.6 6.6l2.2-2.2a1 1 0 0 1 1-.25 11.4 11.4 0 0 0 3.6.57 1 1 0 0 1 1 1V20a1 1 0 0 1-1 1A17 17 0 0 1 3 4a1 1 0 0 1 1-1h3.5a1 1 0 0 1 1 1c0 1.25.2 2.45.57 3.6a1 1 0 0 1-.25 1z"/></svg>
      <span class="phone">0400-555-019</span>
    </li>
    <li>
      <svg viewBox="0 0 24 24" aria-hidden="true"><path d="M2 5h20v14H2z M2 5l10 8 10-8" fill="var(--maroon)"/><path d="M3 6l9 7 9-7" fill="none" stroke="#fff" stroke-width="1.6"/></svg>
      <span>info@coralbendpastoral.com.au</span>
    </li>
    <li>
      <svg viewBox="0 0 24 24" aria-hidden="true"><circle cx="12" cy="12" r="10"/><path d="M2 12h20M12 2c3 3 3 17 0 20M12 2c-3 3-3 17 0 20" fill="none" stroke="#fff" stroke-width="1.4"/></svg>
      <span>www.coralbendpastoral.com.au</span>
    </li>
  </ul>
</section>

</body>
</html>
```